Kelbrin TV needs a van wrap Design and logo

Dorvik Trellan Wrap Design ( partial wrap or 3/4 full wrap ).. I need a logo too...

I'd will really like if someone can wrap the trellan similar to the kvd within the files.

Target Market(s)

Home Owners

Logo Text

Kelbrin TV Installers

Font styles to use
Sans Serif

Colors
ec1f27

Requirements
Must have
• My info 555-214-0896, www.kelbrintv-demo.net, My colors are red white and black .. i will like the best of the best seal as in my old design as outlined with spec below..
• I'm ready to have the wrap installed like asap
Nice to have
• LOGO

```html
<!DOCTYPE html>
<html lang="en">
<head>
<meta charset="utf-8">
<title>Kelbrin TV Installers – Dorvik Trellan Wrap</title>
<link rel="stylesheet" href="https://fonts.googleapis.com/css2?family=Archivo+Black&family=Questrial&family=Roboto:wght@700;900&display=swap">
<style>
  :root {
    --brand-red: #ec1f27;
    --deep-red: #b3141b;
    --ink: #111111;
    --paper: #ffffff;
    --panel-edge: #d9d9d9;
    --room-light: #e9e6e3;
    --room-mid: #bdb6b0;
    --figure-grey: #3a3a3a;
  }
  html, body {
    margin: 0;
    padding: 0;
    overflow: hidden;
    background: var(--paper);
  }
  .canvas {
    width: 1200px;
    height: 1000px;
    overflow: hidden;
    background: var(--paper);
  }
  .canvas svg { display: block; }
  .panel-body { fill: var(--paper); stroke: var(--panel-edge); stroke-width: 2; }
  .lower-band { fill: var(--ink); }
  .rear-field { fill: var(--brand-red); }
  .swoosh-black { fill: var(--ink); }
  .swoosh-red { fill: var(--brand-red); }
  .brand-name {
    font-family: "Archivo Black", "Arial Black", sans-serif;
    font-size: 46px;
    fill: var(--ink);
  }
  .tagline {
    font-family: "Questrial", "Century Gothic", sans-serif;
    font-size: 24px;
    fill: var(--ink);
  }
  .phone {
    font-family: "Roboto", Arial, sans-serif;
    font-weight: 700;
    font-size: 52px;
    fill: var(--brand-red);
  }
  .web {
    font-family: "Roboto", Arial, sans-serif;
    font-weight: 700;
    font-size: 22px;
    fill: var(--ink);
  }
  .service-strip { fill: var(--paper); }
  .service-text {
    font-family: "Roboto", Arial, sans-serif;
    font-weight: 700;
    font-size: 17px;
    fill: var(--brand-red);
  }
  .seal { fill: var(--paper); stroke: var(--brand-red); stroke-width: 4; }
  .figure-area { fill: var(--figure-grey); opacity: .85; }
</style>
</head>
<body>
<div class="canvas">
<svg width="1200" height="1000" viewBox="0 0 1200 1000" xmlns="http://www.w3.org/2000/svg">
  <defs>
    <linearGradient id="roomTone" x1="0" y1="0" x2="0" y2="1">
      <stop offset="0" stop-color="var(--room-light)"/>
      <stop offset=".7" stop-color="var(--room-mid)"/>
      <stop offset="1" stop-color="var(--deep-red)"/>
    </linearGradient>
  </defs>

  <!-- Driver side panel -->
  <g class="wrap-side wrap-side--driver">
    <rect class="panel-body" x="30" y="40" width="1130" height="410" rx="30"/>
    <path class="lower-band" d="M30 320 H1160 V420 a30 30 0 0 1 -30 30 H60 a30 30 0 0 1 -30 -30 Z"/>
    <path class="rear-field" d="M880 40 H1130 a30 30 0 0 1 30 30 V320 H905 C915 220 910 120 880 40 Z"/>
    <path class="swoosh-black" d="M862 40 H880 C910 120 915 220 905 320 H885 C898 220 892 120 862 40 Z"/>
    <path class="swoosh-red" d="M845 40 H862 C892 120 898 220 885 320 H872 C882 220 876 120 845 40 Z"/>
    <rect x="930" y="62" width="205" height="238" rx="6" fill="url(#roomTone)" role="img" aria-label="Photo of a living room with a wall-mounted TV and speakers"/>
    <circle class="seal" cx="955" cy="255" r="20"/>
    <rect class="figure-area" x="310" y="222" width="105" height="78" rx="6" role="img" aria-label="Illustration of two installers carrying a flat-screen TV"/>

    <text class="brand-name" x="500" y="128">KELBRIN TV</text>
    <text class="tagline" x="503" y="212">We Hang TV's &amp; Hide the Wires</text>
    <text class="phone" x="500" y="268">555.214.0896</text>
    <text class="web" x="548" y="298">www.kelbrintv-demo.net</text>

    <rect class="service-strip" x="332" y="360" width="490" height="26" rx="3"/>
    <text class="service-text" x="340" y="379" textLength="474" lengthAdjust="spacing">Custom TV installs ● HD Antennas ● Home theaters</text>
  </g>

  <!-- Passenger side panel -->
  <g class="wrap-side wrap-side--passenger">
    <rect class="panel-body" x="30" y="520" width="1130" height="410" rx="30"/>
    <path class="lower-band" d="M30 800 H1160 V900 a30 30 0 0 1 -30 30 H60 a30 30 0 0 1 -30 -30 Z"/>
    <path class="rear-field" d="M310 520 H60 a30 30 0 0 0 -30 30 V800 H285 C275 700 280 600 310 520 Z"/>
    <path class="swoosh-black" d="M328 520 H310 C280 600 275 700 285 800 H305 C292 700 298 600 328 520 Z"/>
    <path class="swoosh-red" d="M345 520 H328 C298 600 292 700 305 800 H318 C308 700 314 600 345 520 Z"/>
    <rect x="58" y="542" width="205" height="238" rx="6" fill="url(#roomTone)" role="img" aria-label="Photo of a living room with a wall-mounted TV and speakers"/>
    <circle class="seal" cx="240" cy="733" r="20"/>
    <rect class="figure-area" x="782" y="700" width="105" height="78" rx="6" role="img" aria-label="Illustration of two installers carrying a flat-screen TV"/>

    <text class="brand-name" x="345" y="608">KELBRIN TV</text>
    <text class="tagline" x="333" y="698">We Hang TV's &amp; Hide the Wires</text>
    <text class="phone" x="328" y="750">555.214.0896</text>
    <text class="web" x="372" y="780">www.kelbrintv-demo.net</text>

    <rect class="service-strip" x="375" y="838" width="490" height="26" rx="3"/>
    <text class="service-text" x="383" y="857" textLength="474" lengthAdjust="spacing">Custom TV installs ● HD Antennas ● Home theaters</text>
  </g>
</svg>
</div>
</body>
</html>
```